Business Cards for IT Consulting Company (Managed Service Provider)

I am looking to have some business cards printed and would like some designs. We are an IT Consulting company based in Vancouver BC. I would like a nice clean and modern look to the cards. I have uploaded all the versions of my logo so parts can be used as needed. Here is a snippit from our website homepage:

Kelbrook Systems Ltd. is an IT Solutions Partner located in Vancouver BC, Canada. We offer IT solutions and support to customers in the greater Vancouver Area. With expertise in Microsoft platforms, as well as Linux and Mac OSX and over 12 years experience in the IT industry, Kelbrook Systems is dedicated to offering our clients top quality service and products. We take pride in the solutions we offer our customers. The greatest compliment a client can give us is to recommend our services.

Kelbrook Systems Ltd. offers a wide range of IT services from onsite service to remote support and managed service solutions. This allows clients to choose the support path that best suits their company’s needs. Supporting many different sized companies from small to enterprise level over the past 12 years Kelbrook Systems has the experience and expertise needed to ensure things run smoothly. Allowing our clients to focus on doing business.

Revolutionizing the way IT services are delivered.

Kelbrook Systems is dedicated to providing our clients with IT solutions that work and grow with them for years to come. This philosophy helps save money in the long run instead of replacing equipment constantly. Far too often IT solutions are not well thought out and while possibly solving the problem at hand, require replacement due to growth or quality within a very short time frame. Kelbrook Systems takes pride in providing solutions that will last and be able to accommodate growth without the need for replacement.

Industry/Entity Type

Information Technology

Contact Information for Business Card

Kelbrook Systems Ltd.
(Employee Name)
Eml: (Employees Email Address)
Web: kelbrook.me
Ph: 604-555-0142

Font styles to use
Serif
Sans Serif

Requirements
Must have
• The Company logo and company colors.
Nice to have
• - Our tag line: "Revolutionizing IT Services" or "Revolutionizing the way IT services are delivered."
• - Also I really like the idea of nature and technology together blending which is sort of where my logo came from so integrating that somehow onto the business cards would be great.

```html
<!DOCTYPE html>
<html lang="en">
<head>
<meta charset="utf-8">
<title>Kelbrook Systems Ltd. — Business Card</title>
<link rel="stylesheet" href="https://fonts.googleapis.com/css2?family=Ubuntu:wght@400;700&display=swap">
<style>
  :root {
    --page-bg: #e9e7e4;
    --card-white: #ffffff;
    --brand-blue: #27a9e1;
    --brand-green: #8cc63f;
    --ink-dark: #2b2b2b;
    --text-light: #ffffff;
    --card-radius: 64px;
  }
  * { margin: 0; padding: 0; box-sizing: border-box; }
  html, body {
    width: 1200px;
    height: 1200px;
    overflow: hidden;
    background: var(--page-bg);
    font-family: "Ubuntu", sans-serif;
  }
  .canvas {
    position: relative;
    width: 1200px;
    height: 1200px;
  }
  .card {
    position: absolute;
    left: 300px;
    width: 600px;
    height: 360px;
    border-radius: 0 var(--card-radius) 0 var(--card-radius);
    box-shadow: 0 10px 28px rgba(0, 0, 0, 0.18);
    overflow: hidden;
  }
  .card--front {
    top: 190px;
    background: var(--card-white);
    display: flex;
    align-items: center;
    justify-content: center;
  }
  .brand-name {
    color: var(--brand-blue);
    font-weight: 700;
    font-size: 44px;
    letter-spacing: 0.5px;
    display: flex;
    align-items: center;
    gap: 16px;
  }
  .brand-mark {
    width: 34px;
    height: 34px;
    background: var(--brand-blue);
  }
  .card--back {
    top: 650px;
    background: var(--brand-blue);
    color: var(--text-light);
  }
  .employee-name {
    position: absolute;
    left: 42px;
    top: 108px;
    font-size: 20px;
    font-weight: 700;
    letter-spacing: 0.5px;
  }
  .contact-list {
    position: absolute;
    left: 42px;
    top: 162px;
    list-style: none;
    font-size: 19px;
    font-weight: 400;
    line-height: 1.4;
  }
  .pattern-area {
    position: absolute;
    right: 0;
    top: 0;
    width: 230px;
    height: 100%;
    background: linear-gradient(160deg, #3cb4e4 0%, #6fbf6a 55%, #8cc63f 100%);
    opacity: 0.85;
  }
</style>
</head>
<body>
  <main class="canvas">
    <section class="card card--front" aria-label="Card front">
      <div class="brand-name"><span class="brand-mark"></span>Kelbrook Systems</div>
    </section>

    <section class="card card--back" aria-label="Card back">
      <h1 class="employee-name">ABCX TRGS</h1>
      <ul class="contact-list">
        <li>Eml: (Employees Email Address)</li>
        <li>Web: kelbrook.me</li>
        <li>Ph: 604-555-0142</li>
      </ul>
      <div class="pattern-area" role="img" aria-label="Decorative hexagon and cube pattern in outline with green accents"></div>
    </section>
  </main>
</body>
</html>
```